Restaurant business revamping our look and need a new modern menu

We need a new menu that is appealing, similar to the look of our new logo while also keeping our "cozy, clean, Midland staple" feel and gets peoples eyes on the high price items and top sellers. We are a deli that's been around since 1984, with lots of Burgers, Curly Fries, Reuben, Salads, etc.
Once we like that menu, we will need our pizza specials menu updated to look similar.

Please refer to our website for menu word format www.tolbertsofcrestvale.com

Target Market(s)

Every day Midlanders

Industry/Entity Type

Restaurant

Requirements
Must have
• Current menu is a trifold - not a must have but nice layout

```html
<!DOCTYPE html>
<html lang="en">
<head>
<meta charset="utf-8">
<title>Tolbert's Deli Menu</title>
<link href="https://fonts.googleapis.com/css2?family=Oswald:wght@500&family=Bitter:ital,wght@0,400;1,400&family=Alfa+Slab+One&family=Archivo+Black&display=swap" rel="stylesheet">
<style>
:root{
  --ink:#3a3a3a;
  --ink-soft:#555;
  --panel:#424242;
  --paper:#ffffff;
  --on-panel:#f2f2f2;
}
*{margin:0;padding:0;box-sizing:border-box}
html,body{width:1200px;height:849px;overflow:hidden;background:var(--paper)}
.menu{position:relative;width:1200px;height:849px;color:var(--ink);font-family:'Bitter',serif}
.abs{position:absolute}

.photo-strip{left:0;top:20px;width:56px;height:790px;background:linear-gradient(180deg,#bcbcbc 0%,#c99a55 20%,#b37a3a 50%,#d7a765 75%,#8a6a48 100%);clip-path:polygon(20% 0,100% 3%,92% 100%,0 98%,0 4%)}

.legend{top:9px;left:466px;font-size:13px;display:flex;gap:48px;align-items:center}
.legend span{display:flex;align-items:center;gap:6px}

.slab{font-family:'Alfa Slab One',serif;line-height:.78;color:var(--ink)}
.cold-title{left:55px;top:40px;font-size:30px}
.cold-title span{display:block}
.cold-title span:nth-child(2){padding-left:12px}
.cold-title span:nth-child(3){padding-left:33px}
.intro{left:215px;top:48px;width:214px;text-align:right;font-size:11.2px;line-height:1.17}

.item{display:flex;justify-content:space-between;align-items:baseline;line-height:15px}
.name{font-family:'Oswald',sans-serif;font-weight:500;font-variant:small-caps;font-size:13.5px;letter-spacing:.4px;line-height:15px}
.price{font-family:'Oswald',sans-serif;font-weight:500;font-size:12px;line-height:15px}
.desc{font-style:italic;font-size:8.6px;line-height:10.4px;color:var(--ink-soft)}
.opt{display:flex;justify-content:space-between;font-size:9.6px;line-height:10.6px}
.opt .price{font-size:9.5px;font-weight:500;line-height:10.6px}
.opt.indent span:first-child{padding-left:34px}
.entry{margin-bottom:5px}

.cold{left:68px;top:126px;width:361px}
.cold .desc{width:270px}

.frame{border:4px solid var(--ink)}
.hot-box{left:56px;top:370px;width:368px;height:452px;border-top-width:5px}
.hot-title{left:283px;top:360px;font-size:30px;background:var(--paper);padding:0 4px}
.hot-title span{display:block}
.hot-title span:nth-child(2){padding-left:22px}
.hot-title span:nth-child(3){padding-left:44px}
.hot{left:74px;top:391px;width:332px}
.hot .entry{margin-bottom:4px}
.hot .desc{width:225px}
.hot .narrow{width:210px}

.mid-top{left:442px;top:38px;width:373px;height:181px;border-top:0}
.midtop{left:458px;top:40px;width:342px}
.midtop .desc{width:220px}

.sides-title{left:722px;top:228px;font-size:29px}
.sides-lead{left:507px;top:238px;font-size:12px}
.sides{left:458px;top:272px;width:342px}
.sides .item{height:19px}
.sides .name{font-size:14px}

.salad-box{left:442px;top:453px;width:373px;height:370px;border-top-width:5px}
.salad-title{left:593px;top:437px;font-size:27px;background:var(--paper);padding:0 4px}
.salad-title span{display:block}
.salad-title span:nth-child(2){padding-left:10px}
.salads{left:458px;top:482px;width:342px}
.salads .desc{width:230px}
.salads .entry{margin-bottom:2px}

.right-top{left:826px;top:38px;width:362px;height:101px;border-top:0}
.righttop{left:840px;top:42px;width:334px}
.righttop .desc{width:210px}

.burger-panel{left:828px;top:155px;width:360px;height:442px;background:var(--panel);color:var(--on-panel)}
.burger-title{left:840px;top:165px;font-family:'Archivo Black',sans-serif;font-size:33px;line-height:.9;color:var(--on-panel);letter-spacing:1px}
.addons{left:1000px;top:190px;width:178px;font-size:11.5px;color:var(--on-panel)}
.addons .opt{font-size:11.5px;line-height:17.5px}
.addons .price{font-size:11px;line-height:17.5px}
.burgers{left:840px;top:262px;width:338px;color:var(--on-panel)}
.burgers .desc{color:#ddd;width:225px}
.burgers .entry{margin-bottom:6px}

.food-photo{left:826px;top:606px;width:346px;height:152px;background:radial-gradient(ellipse at 40% 40%,#b98540 0%,#7a5a30 28%,#4f7a36 55%,#2f5224 100%);clip-path:polygon(4% 8%,30% 2%,70% 5%,98% 0,96% 60%,100% 95%,60% 100%,20% 96%,0 90%,2% 40%)}
.address{left:826px;top:762px;width:362px;text-align:center;font-style:italic;font-size:14px;line-height:18px}
.web{left:829px;top:799px;display:flex;align-items:center;gap:8px;font-family:'Oswald',sans-serif;font-size:12.5px}
.social{left:1086px;top:799px;display:flex;align-items:center;gap:8px;font-family:'Oswald',sans-serif;font-size:12.5px}
.dot{width:17px;height:17px;border-radius:50%;background:var(--ink)}
.sq{width:16px;height:16px;border-radius:3px;background:var(--ink)}
</style>
</head>
<body>
<main class="menu">
  <div class="abs photo-strip" role="img" aria-label="Photo of golden curly fries"></div>

  <div class="abs legend">
    <span>
      <svg width="30" height="12" viewBox="0 0 30 12"><path d="M1 2h28" stroke="#3a3a3a" stroke-width="2"/><path d="M2 2h11v4a5 5 0 0 1-11 0z M17 2h11v4a5 5 0 0 1-11 0z" fill="#3a3a3a"/></svg>
      - Summer Special
    </span>
    <span>
      <svg width="14" height="16" viewBox="0 0 14 16"><path d="M3 9l-2 6 3-1 2 2 1-5 1 5 2-2 3 1-2-6" fill="#3a3a3a"/><circle cx="7" cy="6" r="5" fill="#3a3a3a"/><circle cx="7" cy="6" r="3" fill="#fff"/></svg>
      - must try/recommen
    </span>
  </div>

  <!-- Cold sandwiches -->
  <h2 class="abs slab cold-title"><span>COLD</span><span>SAND</span><span>WICH</span></h2>
  <p class="abs intro">All sandwiches served on your choice of bread: croissant... jalapeño bun... white... whole wheat... or rye and Tolbert's home-made mayonnaise sauce (unless requested dry)</p>
  <section class="abs cold">
    <div class="entry"><div class="item"><span class="name">B2LT</span><span class="price">8.50</span></div><p class="desc">A standard BLT with extra bacon.</p></div>
    <div class="entry"><div class="item"><span class="name">Club Sandwich</span><span class="price">10.09</span></div><p class="desc">the traditional favorite (ham, turkey, and bacon, triple-decker) enhanced by Tolbert's quality and quantity.</p></div>
    <div class="entry"><div class="item"><span class="name">Califonia Club</span><span class="price">10.09</span></div><p class="desc" style="width:300px">ham, turkey, avocado, sprouts, tomato, and black olives on a croissant.</p></div>
    <div class="entry"><div class="item"><span class="name">Turk-Ado</span><span class="price">10.09</span></div><p class="desc">Triple decker sandwich with turkey, avocado, bacon &amp; sprouts.</p></div>
    <div class="entry" style="margin-top:4px;margin-bottom:4px"><div class="item"><span class="name">Chicken Salad Sandwich</span><span class="price">7.75</span></div></div>
    <div class="entry"><div class="item"><span class="name">Tuna or Krab Salad Sandwich</span><span class="price">8.75</span></div></div>
    <div class="entry"><div class="item"><span class="name">Chicken Caesar Wrap <svg width="22" height="9" viewBox="0 0 30 12"><path d="M1 2h28" stroke="#3a3a3a" stroke-width="2"/><path d="M2 2h11v4a5 5 0 0 1-11 0z M17 2h11v4a5 5 0 0 1-11 0z" fill="#3a3a3a"/></svg></span><span class="price">10.00</span></div><p class="desc">Romaine, parm, and our grilled chicken wrapped in a delicious tortilla with our homemade Caesar dressing</p></div>
  </section>

  <!-- Hot sandwiches -->
  <div class="abs frame hot-box"></div>
  <h2 class="abs slab hot-title"><span>HOT</span><span>SAND</span><span>WICH</span></h2>
  <section class="abs hot">
    <div class="entry narrow"><div class="item"><span class="name">Grilled Cheese Sandwich</span><span class="price">6.25</span></div><p class="desc">Grilled with your choice od Swiss, provolone, American cheddar or pepper jack.</p></div>
    <div class="entry narrow"><div class="item"><span class="name">Beer Brats</span><span class="price">6.50</span></div><p class="desc">Soaked in beer with grilled onions and sauerkraut on a toasted French roll.</p></div>
    <div class="entry"><div class="item"><span class="name">Beefeater</span><span class="price">9.35</span></div><p class="desc">Thin sliced roast beef on white bread with horseradish sauce, melted Swiss and tomato slices.</p></div>
    <div class="entry"><div class="item"><span class="name">French Dip</span><span class="price">9.05</span></div><p class="desc">Lean roast beef served on a steak bun with au jus...c'est magnifique!</p></div>
    <div class="entry"><div class="item"><span class="name">Philly</span><span class="price">10.35</span></div><p class="desc">Lean roast beef with grilled onions and cheddar cheese on a fresh-baked French roll.</p></div>
    <div class="entry"><div class="item"><span class="name">Reuben</span><span class="price">10.05</span></div><p class="desc">Lean corned beef on grilled rye with melted Swiss, Reuben dressing and saurkraut...mmm good!</p></div>
    <div class="entry"><div class="item"><span class="name">Rachel (Turkey Reuben)</span><span class="price">10.05</span></div><p class="desc">Turkey on grilled rye with melted Swiss, Rueben dressing and saurkraut.</p></div>
    <div class="entry"><div class="item"><span class="name">Krabmelt</span><span class="price">10.35</span></div><p class="desc" style="width:260px">Fresh krab salad, melted Swiss served on grilled rye bread.</p></div>
    <div class="entry"><div class="item"><span class="name">Grilled Chicken Sandwich</span><span class="price">9.75</span></div><p class="desc">Strip grilled chicken breast served on a toasted bun with lettuce and tomato.</p></div>
    <div class="entry"><div class="item"><span class="name">Blackened Chicken Sandwich</span><span class="price">9.75</span></div><p class="desc">Strip of blackened chicken breast served on a whole wheat bun with lettuce and tomato</p></div>
  </section>

  <!-- Middle top -->
  <div class="abs frame mid-top"></div>
  <section class="abs midtop">
    <div class="entry"><div class="item"><span class="name">Chik-Ado</span><span class="price">10.15</span></div><p class="desc" style="width:230px">Strips of marinated chicken on a wheat bun topped with bacon, pepper jack cheese, sprouts and avocado.</p><p class="desc" style="font-size:7.6px;width:240px">(Delicious variation on a jalapeno bun with a side of ranch!)</p></div>
    <div class="entry"><div class="item"><span class="name">Chicken Fried Steak Sandwich</span><span class="price">10.05</span></div><p class="desc">with lettuce and tomato on a toasted bun.</p></div>
    <div class="entry"><div class="item"><span class="name">Veggie Pita</span><span class="price">13.09</span></div><p class="desc">Fresh garden veggies sautéed with olive oil, seasoned &amp; served in a pita pocket</p>
      <div class="opt"><span>Grilled or Blackened Chicken Breast</span><span class="price">15.05</span></div>
      <div class="opt"><span>Grilled or Blackened Shrimp</span><span class="price">14.09</span></div>
      <div class="opt indent"><span>+ add 4oz Hummus</span><span class="price">2.25</span></div>
      <div class="opt indent"><span>+ add 4oz Tzatziki</span><span></span></div>
    </div>
  </section>

  <!-- Sides -->
  <p class="abs sides-lead">Choose the following sides:</p>
  <h2 class="abs slab sides-title">SIDES</h2>
  <section class="abs sides">
    <div class="item"><span class="name">Potato Salad</span><span class="price">2.25</span></div>
    <div class="item"><span class="name">Cole Slaw</span><span class="price">2.25</span></div>
    <div class="item"><span class="name">Potato Chips</span><span class="price">2.25</span></div>
    <div class="item"><span class="name">Pasta Salad</span><span class="price">2.25</span></div>
    <div class="item"><span class="name">Ranch Style Beans</span><span class="price">2.25</span></div>
    <div class="item"><span class="name">Mixed Fruit Cup</span><span class="price">2.25</span></div>
    <div class="item"><span class="name">Curly “Q” Fries</span><span class="price">2.25</span></div>
    <div class="item"><span class="name">Sweet Potato Curly Fries</span><span class="price">4.00</span></div>
  </section>

  <!-- Salads -->
  <div class="abs frame salad-box"></div>
  <h2 class="abs slab salad-title"><span>SAL</span><span>ADS</span></h2>
  <section class="abs salads">
    <div class="entry"><div class="item"><span class="name">Chicken Salad Plate</span><span class="price">9.95</span></div><p class="desc" style="width:240px">Chicken salad served on tomato wedge or avocado half, with Swiss and cheddar cheese and a side order of your choice.</p></div>
    <div class="entry"><div class="item"><span class="name">Tuna or Krab Salad Plate</span><span class="price">10.75</span></div><p class="desc" style="width:240px">Tuna or Krab salad served on tomato wedge or avocado half, with Swiss and cheddar cheese and a side order of your choice.</p></div>
    <div class="entry"><div class="item"><span class="name">Caesar Salad</span><span class="price">6.09</span></div>
      <div class="opt"><span>with grilled or blackened chicken breast</span><span class="price">8.09</span></div>
      <div class="opt"><span>with grilled or blackened tuna, salmon or shrimp</span><span class="price">10.09</span></div></div>
    <div class="entry"><div class="item"><span class="name">Heavenly Salad</span><span class="price">11.05</span></div><p class="desc">Romaine lettuce, bacon bits, grilled chicken, mandarin oranges, toasted almonds with poppy seed dressing.</p></div>
    <div class="entry"><div class="item"><span class="name">Super Spinach Salad</span><span class="price">11.05</span></div><p class="desc">Baby spinach, eggs, purple onions, bacon bits, roasted red peppers, and bleu cheese crumbles.</p>
      <div class="opt"><span>with grilled or blackened chicken</span><span class="price">13.05</span></div>
      <div class="opt"><span>with grilled or blackened tuna, salmon or shrimp</span><span class="price">15.05</span></div></div>
    <div class="entry"><div class="item"><span class="name">Turkey Bowl</span><span class="price">11.05</span></div><p class="desc">A Caesar salad topped with pasta salad, cubed turkey breast, and fresh grated parmesan</p></div>
    <div class="entry"><div class="item"><span class="name">Chef Salad</span><span class="price">11.05</span></div><p class="desc" style="width:260px">Lettuce, tomato, turkey, ham, shredded cheese, sliced eggs.</p></div>
    <div class="entry"><div class="item"><span class="name">Arugula Salad</span><span class="price">11.25</span></div><p class="desc">Arugula, candied walnuts, thinly sliced green apples dried cranberries, blue cheese, lemon herb vinaigrette.</p></div>
  </section>

  <!-- Right top -->
  <div class="abs frame right-top"></div>
  <section class="abs righttop">
    <div class="opt"><span>with grilled or blackened chicken breast</span><span class="price">13.25</span></div>
    <div class="opt" style="margin-bottom:6px"><span>with blackened salmon, tuna, or chrimp</span><span class="price">15.05</span></div>
    <div class="item"><span class="name">Fit “Chick”</span><span class="price">13.09</span></div>
    <p class="desc">Grilled or blackened chicken served on a bed of spinach with half an avocado and Tolbert's steam grilled veggies with your choice of salad dressing.</p>
    <div class="opt"><span>Sub Grilled or Blackened Salmon, Shrimp or Tuna</span><span class="price">15.05</span></div>
  </section>

  <!-- Burgers and dogs -->
  <div class="abs burger-panel"></div>
  <h2 class="abs burger-title">BURGER<br>AND<br>DOGS</h2>
  <div class="abs addons">
    <div class="opt"><span>Jalapeño Bun <svg width="11" height="13" viewBox="0 0 14 16"><path d="M3 9l-2 6 3-1 2 2 1-5 1 5 2-2 3 1-2-6" fill="#f2f2f2"/><circle cx="7" cy="6" r="5" fill="#f2f2f2"/><circle cx="7" cy="6" r="3" fill="#424242"/></svg></span><span class="price">1.20</span></div>
    <div class="opt"><span>add Fried egg</span><span class="price">1.00</span></div>
    <div class="opt"><span>add cheese</span><span class="price">1.00</span></div>
  </div>
  <section class="abs burgers">
    <div class="entry"><div class="item"><span class="name">Tolbert's Best Burger</span><span class="price">7.09</span></div><p class="desc">100% ground beef on a toasted bun.</p></div>
    <div class="entry"><div class="item"><span class="name">Tolbert's Melt</span><span class="price">8.65</span></div><p class="desc" style="width:260px">100% ground beef with Swiss cheese, served on rye bread.</p></div>
    <div class="entry"><div class="item"><span class="name">Super Burger</span><span class="price">10.39</span></div><p class="desc">Our “Best Burger” enhanced with bacon, avocado, Swiss and cheddar cheese, sprouts, served ona a toasted bun.</p></div>
    <div class="entry"><div class="item"><span class="name">Jalapeño Burger</span><span class="price">10.45</span></div><p class="desc">100% ground beef with pepper jack cheese, bacon and served on a jalapeño bun.</p></div>
    <div class="entry"><div class="item"><span class="name">Green Chile Pepper Burger</span><span class="price">9.95</span></div><p class="desc">100% ground beef with green chile peppers, Swiss cheese on a toasted bun.</p></div>
    <div class="entry"><div class="item"><span class="name">Bacon Jam Arugula Burger</span><span class="price">10.99</span></div><p class="desc">100% ground beef with bacon jam, white cheddar, arugula and drizzle of balsamic reduction on a toasted bun.</p></div>
    <div class="entry"><div class="item"><span class="name">Hotdog</span><span class="price">6.25</span></div><p class="desc">All beef frank.</p></div>
    <div class="entry"><div class="item"><span class="name">Chicago Dog</span><span class="price">7.25</span></div><p class="desc" style="width:290px">All beef frank with chili, cheese, onions and giardiniera relish.</p></div>
    <div class="entry"><div class="item"><span class="name">Mac &amp; Cheese Dog</span><span class="price">7.75</span></div><p class="desc" style="width:290px">All beef Frank with mac &amp; cheese and green onions</p></div>
  </section>

  <div class="abs food-photo" role="img" aria-label="Photo of a spinach salad topped with blackened chicken and red onion"></div>
  <p class="abs address">4820 W. Alder Crestvale, Texas 79014<br>555.014.2277</p>
  <div class="abs web"><span class="dot"></span>www.tolbertsofcrestvale.com</div>
  <div class="abs social"><span class="sq"></span>@tolberts_deli</div>
</main>
</body>
</html>
```